Sing Along Green Goat

We need a couple of brochures made up for a new company Sing Along Green goat. We are offer a creative consulting business for early childhood.

The first brochures is "about us" the presenters of the workshops. We would prefer a coloured background, something funky and bold, even if we could included the colours of the cow's legs. If someone knows how to remove the white background on the logo, that would also be fantastic.
I also like the idea of photo's of the presenters. I will get them too you ASAP
The second brochure is of up coming workshops!

Could we also include on both Brochures: Website: www.singalonggreengoats.com.au
email: info@singalonggreengoats.com.au
Address: 417 Marrabel Street
Caulfield Vic 3162
Phone: 0462 817 904
A.B.N 62-394-257-118

Target Market(s)

Teacher's, early childhood professionals. Owner/operator of childcare. Parent's, after school care.

Industry/Entity Type

Business

```html
<!DOCTYPE html>
<html lang="en">
<head>
<meta charset="utf-8">
<title>Sing Along Green Goat – About Us Brochure</title>
<link rel="stylesheet" href="https://fonts.googleapis.com/css2?family=Andika:wght@400;700&family=Bubblegum+Sans&family=Arimo:wght@700&display=swap">
<style>
  :root {
    --purple: #3a2462;
    --orange: #ef6628;
    --leaf: #68a54a;
    --forest: #136937;
    --lime: #94c94c;
    --pink: #f4939a;
    --sky: #4a8fcf;
    --amber: #f5962b;
    --cocoa: #4a2613;
    --ink: #3a2462;
    --white: #ffffff;
  }
  * { box-sizing: border-box; margin: 0; padding: 0; }
  html, body { width: 1200px; height: 1000px; overflow: hidden; background: var(--white); }
  .canvas { position: relative; width: 1200px; height: 1000px; background: var(--white); }

  .panel { position: absolute; top: 60px; height: 820px; overflow: hidden; }
  .panel--bio { left: 65px; width: 352px; background: var(--pink); }
  .panel--contact { left: 417px; width: 351px; box-shadow: 0 8px 10px rgba(0,0,0,.35); z-index: 2; }
  .panel--cover { left: 768px; width: 356px; }

  .stripes { position: absolute; left: 0; width: 100%; display: flex; }
  .stripes span { flex: 1; box-shadow: 4px 0 6px rgba(0,0,0,.25); }
  .c-purple { background: var(--purple); }
  .c-orange { background: var(--orange); }
  .c-leaf { background: var(--leaf); }
  .c-forest { background: var(--forest); }

  /* bio panel */
  .panel--bio .stripes { top: 0; height: 73px; }
  .bio-name {
    position: absolute; top: 73px; left: 0; width: 100%; height: 59px;
    background: var(--lime); box-shadow: 0 4px 6px rgba(0,0,0,.3);
    font-family: "Bubblegum Sans", sans-serif; font-size: 27px; font-weight: 400; color: var(--cocoa);
    display: flex; align-items: center; justify-content: center;
  }
  .bio-text {
    position: absolute; top: 157px; left: 32px; width: 292px;
    font-family: "Andika", sans-serif; font-size: 13.4px; line-height: 17.5px; letter-spacing: .45px; color: var(--ink);
  }
  .bio-text p + p { margin-top: 17px; }
  .bio-art { position: absolute; left: 0; top: 610px; width: 352px; height: 210px; display: block; }

  /* contact panel */
  .panel--contact .stripes.top { top: 0; height: 145px; }
  .panel--contact .stripes.bottom { top: 583px; height: 237px; }
  .band-blue { position: absolute; left: 0; width: 100%; height: 57px; background: var(--sky); }
  .band-blue.top { top: 145px; }
  .band-blue.bottom { top: 525px; }
  .contact {
    position: absolute; top: 202px; left: 0; width: 100%; height: 323px;
    background: var(--amber); color: var(--white); text-align: center;
    font-family: "Andika", sans-serif; font-weight: 700; font-size: 14.5px; line-height: 19.5px;
    padding-top: 12px;
  }
  .contact .web { font-size: 17px; margin-bottom: 16px; }
  .contact p + p { margin-top: 19px; }
  .contact .abn { font-size: 12px; }

  /* cover panel */
  .cover-top { position: absolute; top: 0; left: 0; width: 100%; height: 387px; background: var(--lime); }
  .cover-art { position: absolute; top: 40px; left: 14px; width: 320px; height: 183px; display: block; }
  .brand-name {
    position: absolute; top: 236px; left: 0; width: 100%; text-align: center;
    font-family: "Andika", sans-serif; font-weight: 400; font-size: 29px; color: var(--cocoa);
  }
  .tagline {
    position: absolute; top: 296px; left: 0; width: 100%; text-align: center;
    font-family: "Arimo", sans-serif; font-weight: 700; font-size: 25px; line-height: 31px; color: var(--white);
  }
  .herd { position: absolute; top: 390px; left: 12px; width: 334px; height: 50px; display: block; }
  .cover-bottom { position: absolute; top: 443px; left: 0; width: 100%; height: 377px; background: var(--purple); }
  .about-title {
    position: absolute; top: 38px; left: 0; width: 100%; text-align: center;
    font-family: "Bubblegum Sans", sans-serif; font-weight: 400; font-size: 38px; color: var(--lime);
  }
  .about-art { position: absolute; top: 112px; left: 0; width: 356px; height: 265px; display: block; }
  .cover-web {
    position: absolute; top: 328px; left: 0; width: 100%; text-align: center;
    font-family: "Andika", sans-serif; font-size: 15px; color: var(--lime); letter-spacing: .6px;
  }
</style>
</head>
<body>
<main class="canvas">

  <section class="panel panel--bio">
    <div class="stripes"><span class="c-purple"></span><span class="c-orange"></span><span class="c-leaf"></span><span class="c-forest"></span></div>
    <h2 class="bio-name">Marla Vennicott</h2>
    <div class="bio-text">
      <p>Marla fell in love with numbers and reading in Grade 1 at school and never looked back. Having indulged in an eclectic range of courses and classes, Marla can crunch the hell out of a budget, explain the art of negotiating with a child with autism or teach you how to dance the tango! Today she is really good at reading between the lines and in our opinion, nobody knows speaks LedgerLine like our Marla can!</p>
      <p>Marla landed in the world of early child-hood 17 years ago and has thrived on being part of a team committed to proving quality care for children and their families. As Finance Manager at Bright Sprouts Management Group, Marla maintains balance and order across all aspects of the business. She has a developed a treasure-trove of skill, techniques, solutions and tricks that she is ready share with Australia's early childhood industry.</p>
    </div>
    <svg class="bio-art" role="img" aria-label="Illustration area: friendly brown mascot animal peeking in from the lower left" viewBox="0 0 352 210" preserveAspectRatio="none">
      <defs>
        <linearGradient id="bioFill" x1="0" y1="0" x2="0" y2="1">
          <stop offset="0" stop-color="#f4939a"/>
          <stop offset="1" stop-color="#8a4a2c"/>
        </linearGradient>
      </defs>
      <rect x="0" y="0" width="352" height="210" fill="url(#bioFill)"/>
    </svg>
  </section>

  <section class="panel panel--contact">
    <div class="stripes top"><span class="c-purple"></span><span class="c-orange"></span><span class="c-leaf"></span><span class="c-forest"></span></div>
    <div class="band-blue top"></div>
    <div class="contact">
      <p class="web">www.singalonggreengoats.com.au</p>
      <p>info@singalonggreengoats.com.au<br>Address: 417 Marrabel Street,<br>Caulfield VIC 3162</p>
      <p>Events Venue: Wattlebank Community<br>Hall, 406 Ferncliff Rd,<br>Caulfield South</p>
      <p>To book a session:<br>call: (03) 9618 4270<br>or email: admin@brightsprouts.com.au<br>Max 20 People per session</p>
      <p class="abn">A.B.N 62-394-257-118</p>
    </div>
    <div class="band-blue bottom"></div>
    <div class="stripes bottom"><span class="c-forest"></span><span class="c-leaf"></span><span class="c-orange"></span><span class="c-purple"></span></div>
  </section>

  <section class="panel panel--cover">
    <div class="cover-top">
      <svg class="cover-art" role="img" aria-label="Illustration area: standing brown mascot animal with coloured legs" viewBox="0 0 320 183" preserveAspectRatio="none">
        <defs>
          <linearGradient id="coverFill" x1="0" y1="0" x2="0" y2="1">
            <stop offset="0" stop-color="#6e4a26"/>
            <stop offset="1" stop-color="#94c94c"/>
          </linearGradient>
        </defs>
        <rect x="0" y="0" width="320" height="183" fill="url(#coverFill)"/>
      </svg>
      <p class="brand-name">sing along green goat</p>
      <p class="tagline">creative consulting<br>for early childhood</p>
    </div>
    <svg class="herd" role="img" aria-label="Illustration area: row of four small mascot animals" viewBox="0 0 334 50" preserveAspectRatio="none">
      <rect x="0" y="0" width="334" height="50" fill="#a98a6e"/>
    </svg>
    <div class="cover-bottom">
      <h1 class="about-title">About us</h1>
      <svg class="about-art" role="img" aria-label="Illustration area: mascot animal head above green grass" viewBox="0 0 356 265" preserveAspectRatio="none">
        <defs>
          <linearGradient id="aboutFill" x1="0" y1="0" x2="0" y2="1">
            <stop offset="0" stop-color="#3a2462"/>
            <stop offset=".45" stop-color="#5a3216"/>
            <stop offset=".75" stop-color="#136937"/>
            <stop offset="1" stop-color="#136937"/>
          </linearGradient>
        </defs>
        <rect x="0" y="0" width="356" height="265" fill="url(#aboutFill)"/>
      </svg>
      <p class="cover-web">www.singalonggreengoats.com.au</p>
    </div>
  </section>

</main>
</body>
</html>
```